Vodka label for New Brand called KIRO Vodka

We need a label measuring 3.5 inches wide & 5 inches tall for this vodka bottle. The brand is "KIRO Vodka". This should be the largest font on the label. "Handcrafted in the USA" should be on bottle in small font near the bottom. The tagline "Keeping It Real Onward" also needs to be included anywhere that makes sense in a smaller font than the brand name. Also in smaller font at the bottom/corners- "80 proof, 750 ml, 40% alc/vol" I value the human mind over AI, but am providing a couple designs that were AI generated to give you a better idea where to start and what we are looking for. Thank you!

Target Market(s)

21-45 year olds.

Industry/Entity Type

Alcohol

Colors
0054AA
0677BA
7BADD7
CADEEF
E8F1F8
EB3D1F
EC4F4E
F09395
F8D3D4
FCEDEE

Requirements
Should not have
• You can not use the US flag but can use elements of it.

```html
<!DOCTYPE html>
<html lang="en">
<head>
<meta charset="utf-8">
<title>KIRO Vodka – Label</title>
<link rel="stylesheet" href="https://fonts.googleapis.com/css2?family=Anton&family=Archivo+Black&family=Teko:wght@500;600&family=Montserrat:wght@600&display=swap">
<style>
  :root {
    --backdrop: #cccccc;
    --navy: #2f5699;
    --red: #e8392b;
    --ink: #111111;
    --white: #ffffff;
    --star: #ffffff;
  }
  html, body {
    margin: 0;
    padding: 0;
    width: 1040px;
    height: 1200px;
    overflow: hidden;
    background: var(--backdrop);
  }
  .canvas {
    position: relative;
    width: 1040px;
    height: 1200px;
  }
  .label {
    position: absolute;
    left: 136px;
    top: 59px;
    width: 768px;
    height: 1082px;
  }
  .band-blue { fill: var(--navy); }
  .stripe-red { fill: var(--red); }
  .stripe-white { fill: var(--white); }
  .star { fill: var(--star); }
  .brand-panel { fill: var(--ink); }
  .body-panel { fill: url(#labelShade); }
  .brand-name {
    font-family: "Anton", "Impact", sans-serif;
    font-size: 272px;
    fill: var(--white);
  }
  .brand-type {
    font-family: "Archivo Black", "Arial Black", sans-serif;
    font-size: 86px;
    fill: var(--white);
  }
  .dot { fill: var(--white); }
  .tagline {
    font-family: "Teko", "Arial Narrow", sans-serif;
    font-weight: 600;
    font-size: 116px;
  }
  .tagline-blue { fill: var(--navy); }
  .tagline-red { fill: var(--red); }
  .info-frame { fill: none; stroke: var(--ink); stroke-width: 3; }
  .info-big {
    font-family: "Teko", "Arial Narrow", sans-serif;
    font-weight: 600;
    fill: var(--ink);
  }
  .info-small {
    font-family: "Teko", "Arial Narrow", sans-serif;
    font-weight: 500;
    fill: var(--ink);
  }
  .info-volume {
    font-family: "Montserrat", "Arial", sans-serif;
    font-weight: 600;
    fill: var(--ink);
  }
</style>
</head>
<body>
<div class="canvas">
  <svg class="label" viewBox="0 0 768 1082" xmlns="http://www.w3.org/2000/svg">
    <defs>
      <linearGradient id="labelShade" x1="0" x2="1" y1="0" y2="0">
        <stop offset="0" stop-color="#d6d6d6"/>
        <stop offset="0.25" stop-color="#ececec"/>
        <stop offset="0.7" stop-color="#e4e4e4"/>
        <stop offset="1" stop-color="#d2d2d2"/>
      </linearGradient>
      <linearGradient id="artShade" x1="0" x2="0" y1="0" y2="1">
        <stop offset="0" stop-color="#8a8a8a"/>
        <stop offset="0.5" stop-color="#3a3a3a"/>
        <stop offset="1" stop-color="#1f1f1f"/>
      </linearGradient>
      <symbol id="starShape" viewBox="-1 -1 2 2">
        <polygon points="0,-1 0.235,-0.324 0.951,-0.309 0.38,0.124 0.588,0.809 0,0.4 -0.588,0.809 -0.38,0.124 -0.951,-0.309 -0.235,-0.324"/>
      </symbol>
    </defs>

    <!-- stars band -->
    <rect class="band-blue" x="0" y="0" width="768" height="99"/>
    <g class="star">
      <use href="#starShape" x="19" y="19" width="32" height="32"/>
      <use href="#starShape" x="81" y="19" width="32" height="32"/>
      <use href="#starShape" x="144" y="19" width="32" height="32"/>
      <use href="#starShape" x="206" y="19" width="32" height="32"/>
      <use href="#starShape" x="269" y="19" width="32" height="32"/>
      <use href="#starShape" x="331" y="19" width="32" height="32"/>
      <use href="#starShape" x="394" y="19" width="32" height="32"/>
      <use href="#starShape" x="456" y="19" width="32" height="32"/>
      <use href="#starShape" x="519" y="19" width="32" height="32"/>
      <use href="#starShape" x="581" y="19" width="32" height="32"/>
      <use href="#starShape" x="644" y="19" width="32" height="32"/>
      <use href="#starShape" x="719" y="19" width="32" height="32"/>
      <use href="#starShape" x="56" y="50" width="32" height="32"/>
      <use href="#starShape" x="119" y="50" width="32" height="32"/>
      <use href="#starShape" x="181" y="50" width="32" height="32"/>
      <use href="#starShape" x="244" y="50" width="32" height="32"/>
      <use href="#starShape" x="306" y="50" width="32" height="32"/>
      <use href="#starShape" x="369" y="50" width="32" height="32"/>
      <use href="#starShape" x="431" y="50" width="32" height="32"/>
      <use href="#starShape" x="494" y="50" width="32" height="32"/>
      <use href="#starShape" x="556" y="50" width="32" height="32"/>
      <use href="#starShape" x="619" y="50" width="32" height="32"/>
      <use href="#starShape" x="681" y="50" width="32" height="32"/>
    </g>

    <!-- stripes -->
    <rect class="stripe-white" x="0" y="99" width="768" height="31"/>
    <rect class="stripe-red" x="0" y="100" width="768" height="4"/>
    <rect class="stripe-red" x="0" y="111" width="768" height="4"/>
    <rect class="stripe-red" x="0" y="122" width="768" height="5"/>

    <!-- brand panel -->
    <rect class="brand-panel" x="0" y="130" width="768" height="372"/>
    <text class="brand-name" x="58" y="383" textLength="636" lengthAdjust="spacingAndGlyphs">KIRO</text>
    <text class="brand-type" x="66" y="457" textLength="642" lengthAdjust="spacing">VODKA</text>
    <g class="dot">
      <circle cx="64" cy="482" r="3"/><circle cx="79" cy="482" r="3"/><circle cx="94" cy="482" r="3"/><circle cx="109" cy="482" r="3"/><circle cx="124" cy="482" r="3"/><circle cx="139" cy="482" r="3"/><circle cx="154" cy="482" r="3"/><circle cx="169" cy="482" r="3"/><circle cx="184" cy="482" r="3"/><circle cx="199" cy="482" r="3"/><circle cx="214" cy="482" r="3"/><circle cx="229" cy="482" r="3"/><circle cx="244" cy="482" r="3"/><circle cx="259" cy="482" r="3"/><circle cx="274" cy="482" r="3"/><circle cx="289" cy="482" r="3"/><circle cx="304" cy="482" r="3"/><circle cx="319" cy="482" r="3"/><circle cx="334" cy="482" r="3"/><circle cx="349" cy="482" r="3"/><circle cx="364" cy="482" r="3"/><circle cx="379" cy="482" r="3"/><circle cx="394" cy="482" r="3"/><circle cx="409" cy="482" r="3"/><circle cx="424" cy="482" r="3"/><circle cx="439" cy="482" r="3"/><circle cx="454" cy="482" r="3"/><circle cx="469" cy="482" r="3"/><circle cx="484" cy="482" r="3"/><circle cx="499" cy="482" r="3"/><circle cx="514" cy="482" r="3"/><circle cx="529" cy="482" r="3"/><circle cx="544" cy="482" r="3"/><circle cx="559" cy="482" r="3"/><circle cx="574" cy="482" r="3"/><circle cx="589" cy="482" r="3"/><circle cx="604" cy="482" r="3"/><circle cx="619" cy="482" r="3"/><circle cx="634" cy="482" r="3"/><circle cx="649" cy="482" r="3"/><circle cx="664" cy="482" r="3"/><circle cx="679" cy="482" r="3"/><circle cx="694" cy="482" r="3"/>
    </g>

    <!-- body panel -->
    <rect class="body-panel" x="0" y="502" width="768" height="580"/>

    <g role="img" aria-label="Engraved illustration of a colonial minuteman in tricorn hat holding a musket">
      <rect x="104" y="512" width="290" height="362" rx="6" fill="url(#artShade)"/>
    </g>

    <text class="tagline tagline-blue" x="404" y="603">KEEPING</text>
    <text class="tagline tagline-blue" x="404" y="686">IT</text>
    <text class="tagline tagline-red" x="404" y="770">REAL</text>
    <text class="tagline tagline-red" x="404" y="853">ONWARD</text>

    <!-- info box -->
    <rect class="info-frame" x="23" y="880" width="723" height="181"/>
    <line class="info-frame" x1="172" y1="880" x2="172" y2="1061"/>
    <line class="info-frame" x1="595" y1="880" x2="595" y2="1061"/>
    <line class="info-frame" x1="172" y1="913" x2="595" y2="913"/>
    <line class="info-frame" x1="172" y1="987" x2="595" y2="987"/>

    <text class="info-big" x="40" y="996" font-size="98">40</text>
    <text class="info-small" x="128" y="996" font-size="32">%</text>
    <text class="info-small" x="97" y="1047" font-size="40" text-anchor="middle" textLength="122" lengthAdjust="spacing">ALC / VOL</text>

    <text class="info-small" x="384" y="966" font-size="42" text-anchor="middle" textLength="346" lengthAdjust="spacingAndGlyphs">HANDCRAFTED IN THE USA</text>
    <text class="info-volume" x="384" y="1043" font-size="32" text-anchor="middle">750<tspan font-size="22">ml</tspan></text>

    <text class="info-big" x="670" y="996" font-size="98" text-anchor="middle">80</text>
    <text class="info-small" x="670" y="1047" font-size="40" text-anchor="middle">PROOF</text>
  </svg>
</div>
</body>
</html>
```